Antibacterial Hand Wash Squeeze Tube Label

We're looking for a contemporary label design for a new Antibacterial Hand Wash for an 8oz squeeze tube. The new consumer brand will be sold to consumers in major US retail stores & online. The moisturizing hand wash contains Aloe Vera, vitamin E, and other natural ingredients so the design should include the color green. Real photos are very effective on packaging, so a picture of Aloe Vera or possibly two hands washing would help draw consumers' attention to the tube on the retail shelf. The front label may wrap around the sides. Rear must be left mostly blank
US Consumers - retail stores & online
Consumer

```html
<!DOCTYPE html>
<html lang="en">
<head>
<meta charset="utf-8">
<title>Antibacterial Hand Wash – Tube Label</title>
<link rel="stylesheet" href="https://fonts.googleapis.com/css2?family=Oswald:wght@400;500&display=swap">
<style>
  :root {
    --backdrop: #eceeed;
    --label-white: #ffffff;
    --ink-dark: #2b2b2b;
    --ink-mid: #3c3c3c;
    --leaf-green: #1f9a2b;
    --leaf-mid: #3fae3a;
    --leaf-deep: #17701d;
    --leaf-pale: #e6f4e2;
  }
  * { margin: 0; padding: 0; box-sizing: border-box; }
  html, body {
    width: 1200px;
    height: 1200px;
    overflow: hidden;
    background: var(--backdrop);
  }
  .canvas {
    position: relative;
    width: 1200px;
    height: 1200px;
  }
  .tube-label {
    position: absolute;
    left: 280px;
    top: 40px;
    width: 640px;
    height: 1120px;
    background: var(--label-white);
    box-shadow: 0 2px 10px rgba(0,0,0,0.08);
    overflow: hidden;
  }
  .product-title {
    position: absolute;
    left: 0;
    right: 0;
    top: 340px;
    text-align: center;
    font-family: "Oswald", sans-serif;
    font-weight: 500;
    font-size: 58px;
    line-height: 1;
    letter-spacing: 0.5px;
    color: var(--ink-dark);
  }
  .product-type {
    position: absolute;
    left: 0;
    right: 0;
    top: 414px;
    text-align: center;
    font-family: "Oswald", sans-serif;
    font-weight: 500;
    font-size: 32px;
    line-height: 1;
    letter-spacing: 1.5px;
    color: var(--ink-mid);
  }
  .ingredient-band {
    position: absolute;
    left: 176px;
    top: 478px;
    width: 288px;
    height: 38px;
    background: var(--leaf-green);
    color: var(--label-white);
    font-family: "Oswald", sans-serif;
    font-weight: 400;
    font-size: 20px;
    line-height: 38px;
    text-align: center;
    letter-spacing: 0.5px;
  }
  .aloe-artwork {
    position: absolute;
    left: 0;
    right: 0;
    bottom: 0;
    height: 580px;
    background:
      radial-gradient(ellipse 70% 85% at 50% 100%,
        var(--leaf-deep) 0%,
        var(--leaf-green) 40%,
        var(--leaf-mid) 62%,
        rgba(63,174,58,0) 100%),
      linear-gradient(180deg,
        rgba(255,255,255,0) 0%,
        var(--leaf-pale) 25%,
        #9fd694 60%,
        var(--leaf-mid) 100%);
  }
</style>
</head>
<body>
  <main class="canvas">
    <section class="tube-label">
      <h1 class="product-title">ANTIBACTERIAL</h1>
      <p class="product-type">HAND WASH</p>
      <p class="ingredient-band">ALOE VERA + VITAMIN E</p>
      <div class="aloe-artwork" role="img" aria-label="Photo-realistic aloe vera plant with tall spiky green leaves rising from the bottom edge of the label, fading softly into white above"></div>
    </section>
  </main>
</body>
</html>
```